Business Card Design

I would like a logo created for the top left corner of the card please. I would like a checkerboard in a dark navy with the edges fading out and one random bright orange square.
Updates

I have attached some further notes and a really rough sketch of what I am after.  Thank you. :)

Target Market(s)

Construction, mining, mechanical

Industry/Entity Type

Business

Contact Information for Business Card

Korvane Works Pty Ltd, Glen Hadwick, P. 0418365072, F. 0736209158, E.glen@korvaneworks.com.au, PO Box 87 YARRAWONGA Q 4581, ABN 53209874611

Font styles to use
Sans Serif

Requirements
Must have
• Really Dark Navy
Really bright Orange

```html
<!DOCTYPE html>
<html lang="en">
<head>
<meta charset="utf-8">
<title>Korvane Works – Business Card</title>
<link rel="stylesheet" href="https://fonts.googleapis.com/css2?family=Poppins:wght@400;600&display=swap">
<style>
  :root {
    --navy: #01067d;
    --navy-soft: rgba(1, 6, 125, 0.45);
    --navy-faint: rgba(1, 6, 125, 0.08);
    --orange: #ff8500;
    --white: #ffffff;
  }
  html, body {
    margin: 0;
    padding: 0;
    overflow: hidden;
    background: var(--white);
  }
  .card {
    position: relative;
    width: 1200px;
    height: 727px;
    overflow: hidden;
    background: var(--white);
    font-family: "Poppins", Arial, sans-serif;
    color: var(--navy);
  }
  .brand-mark {
    position: absolute;
    left: 0;
    top: 0;
    width: 548px;
    height: 549px;
    background: radial-gradient(ellipse at 50% 50%, var(--navy-soft) 0%, rgba(1, 6, 125, 0.3) 60%, var(--navy-faint) 100%);
  }
  .brand-name {
    position: absolute;
    right: 60px;
    top: 128px;
    margin: 0;
    font-size: 64px;
    font-weight: 600;
    line-height: 1;
    white-space: nowrap;
    color: var(--navy);
  }
  .company-name {
    position: absolute;
    right: 60px;
    top: 261px;
    margin: 0;
    font-size: 32px;
    font-weight: 400;
    line-height: 1;
    white-space: nowrap;
  }
  .contact-name {
    position: absolute;
    right: 60px;
    top: 370px;
    margin: 0;
    font-size: 54px;
    font-weight: 600;
    line-height: 1;
    white-space: nowrap;
  }
  .contact-phone {
    position: absolute;
    right: 60px;
    top: 436px;
    margin: 0;
    font-size: 37px;
    font-weight: 400;
    line-height: 1;
    white-space: nowrap;
  }
  .info-band {
    position: absolute;
    left: 0;
    top: 549px;
    width: 1200px;
    height: 178px;
    background: var(--orange);
    color: var(--white);
  }
  .info-line {
    position: absolute;
    margin: 0;
    font-size: 33px;
    font-weight: 400;
    line-height: 1;
    white-space: nowrap;
  }
  .info-line.left { left: 64px; }
  .info-line.right { right: 60px; }
  .info-line.row-1 { top: 55px; }
  .info-line.row-2 { top: 108px; }
</style>
</head>
<body>
  <div class="card">
    <div class="brand-mark" role="img" aria-label="Korvane Works brand mark area"></div>

    <p class="brand-name">Korvane Works</p>
    <p class="company-name">Korvane Works Pty Ltd</p>

    <p class="contact-name">Glen Hadwick</p>
    <p class="contact-phone">0418 365 072</p>

    <div class="info-band">
      <p class="info-line left row-1">PO Box 87 YARRAWONGA Q 4581</p>
      <p class="info-line left row-2">ABN 53 209 874 611</p>
      <p class="info-line right row-1">F. 0736 209 158</p>
      <p class="info-line right row-2">E.glen@korvaneworks.com.au</p>
    </div>
  </div>
</body>
</html>
```